Business Card Design

We require a business card design for a law firm, our signature colours are maroon and cream. Our slogan is "From our family to yours", we would like the cards to be professional however feminine at the same time.

Industry/Entity Type

Business

Contact Information for Business Card

Helena Brackett & Associates Lawyers & Conveyancers, Helena Brackett LL.B. Principal Solicitor, 17 Quillon Street, Marrowdale NSW 2190

Logo styles of interest
Emblem Logo
Abstract Logo
Wordmark Logo

```html
<!DOCTYPE html>
<html lang="en">
<head>
<meta charset="utf-8">
<title>Helena Brackett &amp; Associates — Business Card</title>
<link rel="stylesheet" href="https://fonts.googleapis.com/css2?family=Parisienne&family=EB+Garamond:ital,wght@0,400;0,700;1,400&display=swap">
<style>
  :root {
    --maroon: #5f0a2b;
    --maroon-light: #7a2a43;
    --cream: #f1ddc2;
  }
  * { margin: 0; padding: 0; box-sizing: border-box; }
  html, body {
    width: 1200px;
    height: 741px;
    overflow: hidden;
    background: var(--maroon);
  }
  .card {
    position: relative;
    width: 1200px;
    height: 741px;
    background: var(--maroon);
    color: var(--cream);
    font-family: "EB Garamond", Georgia, serif;
    overflow: hidden;
  }
  .emblem-area {
    position: absolute;
    left: 308px;
    top: 100px;
    width: 536px;
    height: 505px;
  }
  .line {
    position: absolute;
    left: 0;
    width: 100%;
    text-align: center;
    white-space: nowrap;
    line-height: 1;
  }
  .firm-name {
    top: 80px;
    font-family: "Parisienne", "Brush Script MT", cursive;
    font-size: 80px;
    letter-spacing: 0.5px;
  }
  .firm-services {
    top: 206px;
    font-weight: 700;
    font-size: 44px;
    letter-spacing: 0.4px;
  }
  .person-name {
    top: 470px;
    font-size: 50px;
    letter-spacing: 0.5px;
  }
  .person-role {
    top: 512px;
    font-style: italic;
    font-size: 37px;
    padding-left: 10px;
  }
  .address {
    top: 626px;
    font-size: 41px;
    letter-spacing: 0.6px;
  }
</style>
</head>
<body>
  <main class="card">
    <svg class="emblem-area" viewBox="0 0 536 505" role="img" aria-label="Faint emblem decoration behind the text">
      <defs>
        <radialGradient id="emblemGlow" cx="50%" cy="55%" r="55%">
          <stop offset="0%" stop-color="var(--maroon-light)" stop-opacity="0.45"/>
          <stop offset="100%" stop-color="var(--maroon-light)" stop-opacity="0"/>
        </radialGradient>
      </defs>
      <rect width="536" height="505" fill="url(#emblemGlow)"/>
    </svg>

    <h1 class="line firm-name">Helena Brackett &amp; Associates</h1>
    <p class="line firm-services">Lawyers &amp; Conveyancers</p>
    <p class="line person-name">Helena Brackett LL.B.</p>
    <p class="line person-role">Principal Solicitor</p>
    <p class="line address">17 Quillon Street, Marrowdale NSW 2190</p>
  </main>
</body>
</html>
```